Vellora Solutions Website Creation

Create a business website for custom flexible packaging and MDF products. The www.Kestivo.example website is generic page that you can use to create a similar home page for my business.
Specifically: https://www.kestivo.example/packaging/
https://www.kestivo.example/product/mdf-panels/
Domain is Vel-Lora.example
I would like the page to have a more packaging related look than the MDF/wood.

```html
<!DOCTYPE html>
<html lang="en">
<head>
<meta charset="utf-8">
<title>Vellora Solutions – Custom Flexible Packaging</title>
<link href="https://fonts.googleapis.com/css2?family=Roboto:wght@400;500;700&display=swap" rel="stylesheet">
<style>
:root{
  --navy:#1c2a4a;
  --navy-deep:#16223d;
  --blue:#1e8ff0;
  --ink:#1f2430;
  --muted:#5a6272;
  --grey-band:#eef2f6;
  --white:#ffffff;
  --line:#b9dbf9;
}
*{box-sizing:border-box;margin:0;padding:0}
html,body{width:1200px;height:4870px;overflow:hidden}
body{font-family:"Roboto",Arial,sans-serif;color:var(--ink);background:var(--white);position:relative}
.abs{position:absolute}
.blue{color:var(--blue)}
.btn{display:inline-flex;align-items:center;gap:8px;height:44px;padding:0 32px;border-radius:24px;background:var(--blue);color:#fff;font-size:14px;font-weight:500;text-decoration:none;white-space:nowrap}
.btn.dark{background:var(--navy)}
.btn.outline{background:#fff;color:var(--blue);border:1.5px solid var(--blue);height:38px;padding:0 26px;font-size:13px}
.eyebrow{font-size:13px;letter-spacing:2px;color:var(--blue);text-transform:uppercase;text-align:center}
.section-title{font-size:46px;font-weight:500;text-align:center;color:var(--ink)}
.rule{width:230px;height:3px;margin:14px auto 0;background:linear-gradient(90deg,transparent,var(--blue),transparent)}

/* brand lockup: plain dot + name, one colour, one weight */
.brand{display:flex;align-items:center;gap:12px}
.brand-dot{width:26px;height:26px;border-radius:50%;background:var(--blue)}
.brand-name{font-size:28px;font-weight:500;color:var(--navy);line-height:1;white-space:nowrap}

/* header + hero */
.hero{left:0;top:0;width:1200px;height:675px;background:linear-gradient(160deg,#ffffff 0%,#eef5fc 55%,#d9e8f8 100%);overflow:hidden}
.nav{left:415px;top:44px;display:flex;gap:36px;font-size:14px;color:var(--ink)}
.nav .active{border-bottom:2px solid var(--blue);padding-bottom:8px}
.hero h1{left:120px;top:185px;font-size:46px;font-weight:500;line-height:1.12;color:var(--navy)}
.hero p{left:123px;top:368px;font-size:16px;line-height:1.45;width:440px}
.hero-photo{left:620px;top:100px;width:560px;height:520px;border-radius:50% 50% 24px 24px;background:radial-gradient(circle at 55% 45%,#f4f7fb 0%,#c8d7ea 55%,#3c66c8 100%)}

/* categories */
.cats{left:0;top:675px;width:1200px;height:560px}
.card{width:248px;height:300px;border:1.5px solid var(--line);border-radius:6px;text-align:center;padding-top:55px;background:#fff}
.card.dark{background:var(--navy);border-color:var(--navy);color:#fff}
.card h3{font-size:21px;font-weight:500;margin-bottom:14px}
.card li{list-style:none;font-size:13px;line-height:25px;color:var(--muted)}
.card.dark li{color:#dce4f2}
.card .btn{margin-top:14px}
.cat-icon{width:78px;height:78px;border-radius:50%;background:var(--navy);border-top:6px solid var(--blue);display:flex;align-items:center;justify-content:center}
.cat-icon.light{background:var(--blue)}

/* about */
.about-photo{left:92px;top:1280px;width:548px;height:548px;border-radius:50%;background:radial-gradient(circle,#d9dde3 0%,#9aa3ad 70%);border:10px solid var(--navy)}
.about-photo2{left:338px;top:1555px;width:300px;height:300px;border-radius:50%;background:linear-gradient(140deg,#d88b3a,#6d4a2c 60%,#1e3e7a);border:8px solid var(--navy)}
.about-copy{left:678px;top:1315px;width:470px}
.about-copy h2{font-size:48px;font-weight:500;margin:8px 0 40px;color:var(--navy)}
.about-copy p{font-size:17px;line-height:1.6}
.ticks{display:grid;grid-template-columns:210px 240px;gap:28px 8px;margin:38px 0 40px;font-size:13.5px;font-weight:500;color:var(--navy)}
.ticks span{display:flex;align-items:center;gap:8px}

/* products */
.band{left:0;top:1815px;width:1200px;height:955px;background:var(--grey-band)}
.prod-img{border-radius:4px}
.prod-box{padding:42px 44px}
.prod-box h3{font-size:27px;font-weight:500;margin-bottom:22px}
.prod-box p{font-size:14px;line-height:1.6;margin-bottom:20px}

/* why */
.feat h4{font-size:18px;font-weight:700;color:var(--navy)}
.feat p{font-size:12px;line-height:1.6;color:var(--muted);margin-top:6px}
.feat-icon{width:54px;height:54px;border-radius:50%;background:var(--navy);display:flex;align-items:center;justify-content:center}
.feat-icon.blue-bg{background:var(--blue)}

/* industries */
.tile{top:3628px;width:232px;height:246px;display:flex;align-items:flex-end;justify-content:center;padding-bottom:14px;color:#fff;font-size:18px;font-weight:500}

/* cta */
.cta{left:100px;top:3980px;width:1003px;height:515px;border-radius:20px;background:linear-gradient(160deg,#23345a,var(--navy-deep));text-align:center;color:#fff}
.cta h2{font-size:40px;font-weight:500;line-height:1.2;margin-top:56px}
.form{position:absolute;left:210px;top:186px;width:588px;display:grid;grid-template-columns:1fr 1fr;gap:12px 10px}
.field{background:#fff;height:44px;border-radius:3px;color:var(--ink);font-size:13px;text-align:left;padding:14px 24px}
.field.wide{grid-column:1/3;height:94px;padding-top:12px}

/* footer */
.foot-col h5{font-size:15px;font-weight:500;color:var(--navy);margin-bottom:16px}
.foot-col li{list-style:none;font-size:11.5px;line-height:19px;color:var(--muted)}
.bottom{left:0;top:4795px;width:1200px;border-top:1px solid #d8dde4}
.small{font-size:11px;color:var(--muted)}
</style>
</head>
<body>

<section class="abs hero">
  <div class="abs brand" style="left:122px;top:36px">
    <div class="brand-dot"></div>
    <div class="brand-name">Vellora Solutions</div>
  </div>
  <nav class="abs nav">
    <span class="active">Home</span><span>About Us</span><span>Products</span><span>Industries</span><span>Resources</span><span>Contact</span>
  </nav>
  <a class="abs btn" style="left:997px;top:34px;height:40px;padding:0 26px;font-size:13px">Request Quote ›</a>
  <div class="abs hero-photo" role="img" aria-label="Stand-up pouches, vacuum pouches and rolls of stretch film in a blue arc"></div>
  <h1 class="abs">Custom Flexible<br>Packaging Solutions<br><span class="blue">Built for Your Business</span></h1>
  <p class="abs">Vellora Solutions provides high-quality packaging products designed to protect, preserve and perform.</p>
  <a class="abs btn" style="left:120px;top:446px">Request Quote ›</a>
  <a class="abs btn dark" style="left:298px;top:446px">Explore Products ›</a>
</section>

<section class="abs cats">
  <div class="eyebrow" style="margin-top:45px">What we offer</div>
  <h2 class="section-title" style="margin-top:6px">Products <span class="blue">Categories</span></h2>
  <div class="rule"></div>

  <div class="abs card" style="left:82px;top:218px"><h3>Flexible Packaging</h3><ul><li>Vacuum Pouches</li><li>Stand Up Pouches</li><li>Custom Pouches &amp; Bags</li><li>Roll Stock Films</li><li>Shrink Films</li></ul><a class="btn outline">View Products ›</a></div>
  <div class="abs card dark" style="left:350px;top:218px"><h3>Stretch Film</h3><ul><li>Machine Film</li><li>Hand Film</li><li>Coreless Hand Film</li><li>Vented Films</li><li>Banding Film</li></ul><a class="btn outline">View Products ›</a></div>
  <div class="abs card" style="left:618px;top:218px"><h3>Safety Supplies</h3><ul><li>Hand Protection</li><li>Protective Garments</li><li>Eye Protection</li><li>Head Protection</li><li>Face Masks</li><li>Sleeves</li></ul><a class="btn outline">View Products ›</a></div>
  <div class="abs card" style="left:886px;top:218px"><h3>Other Packaging</h3><ul><li>Corrugated Boxes</li><li>Rigid Setup Boxes</li><li>Folding Carton</li><li>V-Board / Corner Board</li><li>Glass &amp; PET Products</li></ul><a class="btn outline">View Products ›</a></div>

  <div class="abs cat-icon" style="left:167px;top:160px"><svg width="34" height="34" viewBox="0 0 34 34" fill="none" stroke="#fff" stroke-width="2"><rect x="8" y="6" width="18" height="24" rx="3"/><path d="M12 20v5h10"/></svg></div>
  <div class="abs cat-icon light" style="left:435px;top:160px"><svg width="36" height="34" viewBox="0 0 36 34" fill="none" stroke="#fff" stroke-width="2"><circle cx="12" cy="17" r="8"/><circle cx="12" cy="17" r="3"/><path d="M12 9h18v16H12"/></svg></div>
  <div class="abs cat-icon" style="left:703px;top:160px"><svg width="32" height="34" viewBox="0 0 32 34" fill="none" stroke="#fff" stroke-width="2"><path d="M16 4l11 4v9c0 7-5 11-11 13C10 28 5 24 5 17V8z"/><path d="M11 17l4 4 7-8"/></svg></div>
  <div class="abs cat-icon light" style="left:971px;top:160px"><svg width="34" height="34" viewBox="0 0 34 34" fill="none" stroke="#fff" stroke-width="2"><path d="M17 5l11 6v12l-11 6-11-6V11z"/><path d="M6 11l11 6 11-6M17 17v12"/></svg></div>
</section>

<div class="abs about-photo" role="img" aria-label="Packaging factory floor with rolls of film"></div>
<div class="abs about-photo2" role="img" aria-label="Colourful folding carton boxes"></div>
<div class="abs about-copy">
  <div class="eyebrow" style="text-align:left">Who we are</div>
  <h2>About <span class="blue">Vellora</span></h2>
  <p>Vellora Solutions is a trusted global supplier of packaging materials and industrial products. We combine quality, innovation and dependable service to help businesses protect their products, improve efficiency and grow with confidence.</p>
  <div class="ticks">
    <span><svg width="18" height="14"><path d="M2 7l5 5 9-10" stroke="#1e8ff0" stroke-width="2.5" fill="none"/></svg>High quality products</span>
    <span><svg width="18" height="14"><path d="M2 7l5 5 9-10" stroke="#1e8ff0" stroke-width="2.5" fill="none"/></svg>Global sourcing &amp; reliability</span>
    <span><svg width="18" height="14"><path d="M2 7l5 5 9-10" stroke="#1e8ff0" stroke-width="2.5" fill="none"/></svg>Competitive pricing</span>
    <span><svg width="18" height="14"><path d="M2 7l5 5 9-10" stroke="#1e8ff0" stroke-width="2.5" fill="none"/></svg>Custom solutions for your needs</span>
  </div>
  <a class="btn" style="height:48px">Request Quote ›</a>
</div>

<section class="abs band">
  <svg class="abs" style="left:0;top:0" width="1200" height="130" viewBox="0 0 1200 130"><path d="M0 0L600 120L1200 0V-2H0z" fill="#fff"/><path d="M0 0L600 120L1200 0" stroke="#8ec7f6" stroke-width="3" fill="none"/></svg>
  <div class="eyebrow" style="margin-top:165px">What we offer</div>
  <h2 class="section-title" style="margin-top:6px">Our <span class="blue">Products</span></h2>
  <div class="rule"></div>

  <div class="abs prod-img" style="left:102px;top:300px;width:493px;height:353px;background:linear-gradient(150deg,#9aa6b5,#e3e8ee 40%,#2a5fc4 75%,#c9a77a)" role="img" aria-label="Assorted stand-up pouches and film rolls"></div>
  <div class="abs prod-box" style="left:133px;top:570px;width:432px;height:260px;background:var(--navy);color:#fff">
    <h3>Custom Flexible <span class="blue">Packaging</span></h3>
    <p>Lorem ipsum dolor sit amet, consectetur adipiscing elit, sed do eiusmod tempor incididunt Lorem ipsum dolor sit amet, consectetur adipiscing elit</p>
    <a class="btn" style="height:38px;padding:0 28px;font-size:13px">Learn More ›</a>
  </div>

  <div class="abs prod-img" style="left:620px;top:295px;width:483px;height:353px;background:linear-gradient(160deg,#f0dfc2,#d9b889 50%,#a98458)" role="img" aria-label="Stacked MDF panels"></div>
  <div class="abs prod-box" style="left:650px;top:583px;width:430px;height:258px;background:#fff">
    <h3>MDF <span class="blue">Products</span></h3>
    <p>Lorem ipsum dolor sit amet, consectetur adipiscing elit, sed do eiusmod tempor incididunt Lorem ipsum dolor sit amet, consectetur adipiscing</p>
    <a class="btn" style="height:38px;padding:0 28px;font-size:13px">Learn More ›</a>
  </div>
</section>

<section class="abs" style="left:0;top:2770px;width:1200px;height:720px">
  <div class="eyebrow" style="margin-top:52px">How it works</div>
  <h2 class="section-title" style="margin-top:6px">Why <span class="blue">Choose Us</span></h2>
  <div class="rule"></div>

  <svg class="abs" style="left:400px;top:170px" width="400" height="400" viewBox="0 0 400 400">
    <path d="M200 10a190 190 0 1 1 -0.1 0" stroke="#1e8ff0" stroke-width="2" fill="none"/>
    <g fill="#fff" stroke="#1e8ff0" stroke-width="3">
      <circle cx="56" cy="76" r="7"/><circle cx="344" cy="76" r="7"/><circle cx="30" cy="270" r="7"/><circle cx="370" cy="270" r="7"/>
    </g>
  </svg>
  <div class="abs" style="left:445px;top:200px;width:310px;height:310px;border-radius:50%;background:radial-gradient(circle,#f3f5f8 30%,#9fb1c6 75%,#3f6fc2)" role="img" aria-label="Collage of packaging production photos"></div>

  <div class="abs feat" style="left:140px;top:182px;width:215px;text-align:right"><h4>Premium Quality</h4><p>We deliver durable, reliable and high-performance products.</p></div>
  <div class="abs feat-icon" style="left:375px;top:180px"><svg width="26" height="26" fill="none" stroke="#fff" stroke-width="2"><circle cx="13" cy="10" r="7"/><path d="M9 16l-2 8 6-3 6 3-2-8"/></svg></div>

  <div class="abs feat-icon" style="left:768px;top:188px"><svg width="26" height="26" fill="none" stroke="#fff" stroke-width="2"><path d="M3 13l6-6 5 4 5-4 5 6-9 8z"/></svg></div>
  <div class="abs feat" style="left:830px;top:190px;width:210px"><h4>Customer Focused</h4><p>We build long-term partnerships through trust and service.</p></div>

  <div class="abs feat" style="left:130px;top:400px;width:210px;text-align:right"><h4>Custom Solutions</h4><p>Tailored packaging solutions to fit your unique requirements.</p></div>
  <div class="abs feat-icon blue-bg" style="left:356px;top:398px"><svg width="26" height="26" fill="none" stroke="#fff" stroke-width="2"><circle cx="13" cy="13" r="5"/><circle cx="13" cy="13" r="10" stroke-dasharray="4 3"/></svg></div>

  <div class="abs feat-icon blue-bg" style="left:786px;top:403px"><svg width="26" height="26" fill="none" stroke="#fff" stroke-width="2"><path d="M5 21C5 10 12 5 22 5c0 10-5 16-15 16M5 21l10-10"/></svg></div>
  <div class="abs feat" style="left:850px;top:396px;width:210px"><h4>Sustainable Options</h4><p>Eco-friendly and recyclable packaging materials available.</p></div>

  <div class="abs feat-icon" style="left:573px;top:568px"><svg width="26" height="26" fill="none" stroke="#fff" stroke-width="2"><rect x="2" y="7" width="14" height="11"/><path d="M16 11h5l3 4v3h-8"/><circle cx="7" cy="20" r="2"/><circle cx="19" cy="20" r="2"/></svg></div>
  <div class="abs feat" style="left:470px;top:628px;width:260px;text-align:center"><h4>Fast &amp; Reliable</h4><p>Tailored packaging solutions to fit your unique requirements.</p></div>
</section>

<h2 class="abs section-title" style="left:0;top:3530px;width:1200px">Industries <span class="blue">Serve</span></h2>
<div class="abs rule" style="left:485px;top:3598px"></div>
<div class="abs tile" style="left:5px;background:linear-gradient(180deg,#f2a81c,#7a4a10)" role="img" aria-label="Bottles of orange juice">Food &amp; Beverages</div>
<div class="abs tile" style="left:246px;background:linear-gradient(180deg,#7f9a55,#3c4a23)" role="img" aria-label="Rows of crops in a field">Agriculture</div>
<div class="abs tile" style="left:488px;background:linear-gradient(180deg,#c89a6a,#5a3b2a)" role="img" aria-label="Shoppers with retail bags">Retail &amp; Ecommerce</div>
<div class="abs tile" style="left:729px;background:linear-gradient(180deg,#7d9bbd,#1f3553)" role="img" aria-label="Tablet in a manufacturing plant">Manufacturing</div>
<div class="abs tile" style="left:970px;background:linear-gradient(180deg,#b6a68a,#4c4a47)" role="img" aria-label="Warehouse aisle with shelving">Logistics &amp; Shipping</div>

<section class="abs cta">
  <h2>Ready to Find the Right<br><span class="blue">Packaging Solution?</span></h2>
  <div class="form">
    <div class="field">First Name</div><div class="field">Last Name</div>
    <div class="field">Email address</div><div class="field">Phone number</div>
    <div class="field wide">Leave Message</div>
  </div>
  <a class="abs btn" style="left:410px;top:414px">Request Quote ›</a>
</section>

<footer>
  <div class="abs brand" style="left:135px;top:4600px">
    <div class="brand-dot"></div>
    <div class="brand-name" style="font-size:26px">Vellora Solutions</div>
  </div>
  <div class="abs" style="left:193px;top:4660px;display:flex;gap:6px">
    <span style="width:24px;height:24px;border-radius:50%;background:var(--blue)"></span>
    <span style="width:24px;height:24px;border-radius:50%;background:var(--navy)"></span>
    <span style="width:24px;height:24px;border-radius:50%;background:var(--navy)"></span>
  </div>
  <div class="abs foot-col" style="left:425px;top:4578px"><h5>Navigation</h5><ul><li>About Us</li><li>Resources</li><li>Careers</li><li>News &amp; Updates</li><li>Contact Us</li></ul></div>
  <div class="abs foot-col" style="left:580px;top:4578px"><h5>Industries</h5><ul><li>Food &amp; Beverage</li><li>Agriculture</li><li>Industrial</li><li>Medical</li><li>Retail</li><li>Logistics</li></ul></div>
  <div class="abs foot-col" style="left:762px;top:4578px"><h5>Products</h5><ul><li>Flexible Packaging</li><li>Stretch Film</li><li>Safety Supplies</li><li>Strapping &amp; Banding</li><li>Other Packaging</li><li>MDF Panels</li></ul></div>
  <div class="abs foot-col" style="left:936px;top:4578px"><h5>Contact</h5>
    <div style="display:flex;gap:10px;align-items:center">
      <span style="width:30px;height:30px;border-radius:50%;background:var(--blue);display:flex;align-items:center;justify-content:center"><svg width="16" height="12" fill="none" stroke="#fff" stroke-width="1.5"><rect x="1" y="1" width="14" height="10"/><path d="M1 1l7 6 7-6"/></svg></span>
      <div class="small" style="line-height:1.4"><b style="color:var(--navy)">Email address</b><br>info@vel-lora.example</div>
    </div>
  </div>
  <div class="abs bottom"></div>
  <div class="abs small" style="left:136px;top:4816px">© 2025 Vellora Solutions. All Rights Reserved.</div>
  <div class="abs small" style="left:880px;top:4816px">Privacy Policy | Terms &amp; Conditions | Sitemap</div>
</footer>

</body>
</html>
```